Brochure Design Project

I am looking for a trifold brochure.
I would like it to be square (5.5 x 5.5)
The back needs to be reserved for a map and logo information.

we are a financial planning firm. we have been in operation for 15 years.
our clients are ecstatic and continue to refer others to us.

Brochure COPY:
Building Wealth, Building Futures
We start with your goals. Then we build a comprehensive strategy to manage your investments, grow your wealth, minimize your tax burden and protect your family. Most importantly, we keep you informed about market change, opportunities and concerns before they impact you, so you can make confident decisions about your future, every step of the way.

Understanding and Expertise (bios)
Steadfast Money Partners is led by Lorna Feldskov and Miriam Oakhurst, experienced business partners who take the time to listen to you, understand your needs and present you with all your options.
Our focus in on your future, and building a confident and financially secure path for you and your family for the years ahead.

Lorna Feldskov, BSc, MBA, CPA, CA, CFP, FMA, CPCA
Certified Financial Planner

With years of experience in tax, investment, estate and retirement issues - and an extensive business background - Lorna provided her clients with important financial insights and clear direction in a friendly and open manner.

Miriam Oakhurst, BSEd, FMA, CPCA, CFP, FCSI, CIM

After a successful tennis career Miriam joined Lorna in the financial industry. Miriam quickly discovered how much she enjoys working with people and helping them to achieve their goals. Leveraging the discipline and work ethic developed during her tennis career, Miriam has been instrumental in creating the successful process used by Steadfast Money Partners.

People Trust Us to Help Them
The important things in life are often neglected due to the demands of day to day, including financial planning and wealth management. But it doesn't have to be that way when you have a trustworthy team looking out for you.
At Steadfast Money Partners we have the knowledge, experience and resources to help you move forward and realize your financial goals.

(side note) on the back of the brochure it should have the SMP logo, the office address, 382 Kettlewood Rd. E. Mississauga, ON L5R 7M4, and our website address.

Reason: Am juggling a number of different projects so need to extend the deadline on this one. Will provide copy for the project by end of day today.

Target Market(s)

We would like the brochure to appeal to the high net worth client who is currently working with an advisor but is not getting the attention from them.

Industry/Entity Type

Financial

Requirements
Must have
• SMP Logo on the front. The logo is blue with black font and has a tagline with it that says "Choose your path, change your future."
you can see the logo at www.plantharvestsoon.ca

One page must be about the two advisors, Lorna Feldskov and Miriam Oakhurst.
(leave an open area for bios and we will fill it in)

We want it to talk about building wealth and passing it on to the next generation.
Should not have
• Financial lingo.

```html
<!DOCTYPE html>
<html lang="en">
<head>
<meta charset="utf-8">
<title>Steadfast Money Partners – Trifold Brochure</title>
<link rel="stylesheet" href="https://fonts.googleapis.com/css2?family=Didact+Gothic&family=Roboto+Condensed:wght@300;400;700&display=swap">
<style>
  :root {
    --stage: #707070;
    --gold: #f3c44f;
    --ink: #111111;
    --blue: #2a68b1;
    --sky: #e4eef8;
    --paper: #ffffff;
    --leaf-light: #a9cf6b;
    --leaf-dark: #4f8a2b;
    --pot: #d9925a;
    --map: #e8e4dc;
    --panel: 360px;
  }
  * { box-sizing: border-box; margin: 0; padding: 0; }
  html, body { width: 1200px; height: 900px; overflow: hidden; }
  body {
    background: var(--stage);
    font-family: "Didact Gothic", "Century Gothic", sans-serif;
    color: var(--ink);
    position: relative;
  }
  .spread {
    position: absolute;
    left: 60px;
    display: flex;
    width: calc(var(--panel) * 3);
    height: var(--panel);
    box-shadow: 0 10px 24px rgba(0,0,0,.35);
  }
  .spread--inside { top: 60px; }
  .spread--outside { top: 480px; }
  .panel {
    position: relative;
    width: var(--panel);
    height: var(--panel);
    overflow: hidden;
  }
  .panel + .panel { border-left: 1px solid rgba(0,0,0,.08); }
  .panel--gold { background: var(--gold); }
  .panel--white { background: var(--paper); }
  .panel--sky { background: var(--sky); }

  /* Inside left: intro + understanding */
  .intro-block {
    position: absolute; left: 18px; top: 26px;
    width: 176px; height: 300px;
  }
  .intro-block svg { position: absolute; inset: 0; }
  .intro-text {
    position: absolute; left: 12px; right: 10px; bottom: 14px;
    color: var(--paper); font-size: 9.6px; line-height: 1.42;
    text-align: justify;
  }
  .expertise {
    position: absolute; left: 206px; top: 118px; width: 140px;
  }
  .heading-thin {
    font-family: "Roboto Condensed", "Arial Narrow", sans-serif;
    font-weight: 300; color: var(--blue); line-height: .9;
    letter-spacing: -.5px;
  }
  .expertise .heading-thin { font-size: 22px; margin-bottom: 8px; }
  .body-small { font-size: 8.4px; line-height: 1.4; }
  .body-small + .body-small { margin-top: 7px; }

  /* Photo placeholders */
  .photo { position: absolute; }
  .photo--topiary {
    left: 0; top: 0; width: 100%; height: 100%;
    background: radial-gradient(circle at 55% 45%, var(--leaf-light) 0 18%, var(--leaf-dark) 24%, #eef0ee 34%, #f4f4f4 70%);
  }
  .photo--cover {
    left: 40px; top: 30px; width: 230px; height: 262px;
    background: radial-gradient(ellipse at 50% 35%, var(--leaf-light) 0 22%, var(--leaf-dark) 32%, rgba(255,255,255,0) 46%),
                radial-gradient(ellipse at 55% 85%, #e8c3a8 0 20%, rgba(255,255,255,0) 40%);
  }
  .photo--map {
    left: 22px; top: 48px; width: 316px; height: 150px;
    background: linear-gradient(135deg, var(--map), #d9d4c9);
    border: 1px solid rgba(0,0,0,.15);
  }

  /* Inside right: advisors */
  .advisor {
    position: absolute; left: 18px; right: 16px;
    display: grid; grid-template-columns: 150px 1fr; column-gap: 12px;
  }
  .advisor--first { top: 28px; }
  .advisor--second { top: 192px; }
  .advisor__id { border-right: 1px solid var(--ink); padding-right: 10px; }
  .advisor__name { font-size: 30px; }
  .advisor__creds {
    font-family: "Roboto Condensed", "Arial Narrow", sans-serif;
    font-weight: 700; font-size: 9.5px; line-height: 1.25; margin-top: 6px;
  }
  .advisor__bio { font-size: 7.8px; line-height: 1.38; }

  /* Outside left: trust */
  .trust { position: absolute; left: 26px; top: 40px; right: 26px; }
  .trust .heading-thin { font-size: 44px; line-height: .82; }
  .trust .body-small { font-size: 9px; margin-top: 22px; width: 230px; margin-left: 60px; }

  /* Outside middle: back */
  .label { position: absolute; left: 22px; top: 28px; font-size: 10px; }
  .brand-block { position: absolute; left: 22px; right: 22px; bottom: 28px; }
  .brand {
    display: flex; align-items: center; gap: 8px;
    font-size: 17px; color: var(--ink);
  }
  .brand__dot { width: 12px; height: 12px; border-radius: 50%; background: var(--blue); }
  .tagline { color: var(--blue); font-size: 10px; margin-top: 3px; }
  .contact { font-size: 10px; line-height: 1.5; margin-top: 12px; }

  /* Outside right: cover */
  .cover-title {
    position: absolute; left: 200px; top: 60px; width: 150px;
    font-family: "Roboto Condensed", "Arial Narrow", sans-serif;
    font-weight: 300; font-size: 24px; line-height: .95; color: var(--ink);
  }
  .cover-title span { display: block; }
  .cover-title .accent { color: var(--blue); }
  .cover-title .indent { margin-left: 14px; }
  .cover-foot {
    position: absolute; left: 0; right: 0; bottom: 0; height: 58px;
    background: var(--paper); padding: 8px 18px 0 0; text-align: right;
    border-top: 1px solid #e6e6e6;
  }
  .cover-foot .brand { justify-content: flex-end; font-size: 18px; }
  .cover-foot .tagline { font-size: 9.5px; }
  .panel--cover { background: linear-gradient(180deg, #ffffff, #e9e9e9); }
</style>
</head>
<body>

<section class="spread spread--inside" aria-label="Brochure inside">
  <article class="panel panel--gold">
    <div class="intro-block">
      <svg viewBox="0 0 176 300" width="176" height="300" aria-hidden="true">
        <path d="M0 40 Q0 0 40 0 L110 0 Q140 0 140 40 L140 78 L176 78 L176 300 L0 300 Z" fill="#111"/>
      </svg>
      <p class="intro-text">We start with your goals. Then we build a comprehensive strategy to manage your investments, grow your wealth, minimize your tax burden and protect your family. Most importantly, we keep you informed about market change, opportunities and concerns before they impact you, so you can make confident decisions about your future, every step of the way.</p>
    </div>
    <div class="expertise">
      <h2 class="heading-thin">understanding<br>and expertise</h2>
      <p class="body-small">Steadfast Money Partners is led by Lorna Feldskov and Miriam Oakhurst, experienced business partners who take the time to listen to you, understand your needs and present you with all your options.</p>
      <p class="body-small">Our focus is on your future, and building a confident and financially secure path for you and your family for the years ahead.</p>
    </div>
  </article>

  <article class="panel panel--white">
    <div class="photo photo--topiary" role="img" aria-label="Photo of a potted topiary trimmed into a rising arrow shape"></div>
  </article>

  <article class="panel panel--gold">
    <div class="advisor advisor--first">
      <div class="advisor__id">
        <h3 class="heading-thin advisor__name">Lorna<br>Feldskov</h3>
        <p class="advisor__creds">BSc, MBA, CPA, CA<br>CFP, FMA, CPCA<br>Certified Financial Planner</p>
      </div>
      <p class="advisor__bio">With years of experience in tax, investment, estate and retirement issues – and an extensive business background – Lorna provides her clients with important financial insights and clear direction in a friendly and open manner.</p>
    </div>
    <div class="advisor advisor--second">
      <div class="advisor__id">
        <h3 class="heading-thin advisor__name">Miriam<br>Oakhurst</h3>
        <p class="advisor__creds">BSEd, FMA, CPCA<br>CFP, FCSI, CIM<br>Certified Financial Planner</p>
      </div>
      <p class="advisor__bio">After a successful tennis career Miriam joined Lorna in the financial industry. Miriam quickly discovered how much she enjoys working with people and helping them achieve their goals. Her discipline and work ethic have been key to the process used by Steadfast Money Partners.</p>
    </div>
  </article>
</section>

<section class="spread spread--outside" aria-label="Brochure outside">
  <article class="panel panel--sky">
    <div class="trust">
      <h2 class="heading-thin">people<br>&nbsp;&nbsp;trust us to<br>&nbsp;&nbsp;&nbsp;&nbsp;help them</h2>
      <p class="body-small">The important things in life are often neglected due to the demands of day to day, including financial planning and wealth management. But it doesn't have to be that way when you have a trustworthy team looking out for you.</p>
      <p class="body-small">At Steadfast Money Partners we have the knowledge, experience and resources to help you move forward and realize your financial goals.</p>
    </div>
  </article>

  <article class="panel panel--gold">
    <p class="label">Location Plan</p>
    <div class="photo photo--map" role="img" aria-label="Street map showing the office location"></div>
    <div class="brand-block">
      <p class="brand"><span class="brand__dot" aria-hidden="true"></span>Steadfast Money Partners</p>
      <p class="tagline">Choose your path, change your future.</p>
      <p class="contact">382 Kettlewood Rd. E. Mississauga, ON L5R 7M4<br>www.plantharvestsoon.ca</p>
    </div>
  </article>

  <article class="panel panel--cover">
    <div class="photo photo--cover" role="img" aria-label="Photo of a hand holding a small pot with a plant trimmed into a dollar sign"></div>
    <h1 class="cover-title">
      <span>Building</span><span class="accent indent">Wealth,</span>
      <span style="margin-top:16px">Building</span><span class="accent indent">Futures</span>
    </h1>
    <div class="cover-foot">
      <p class="brand"><span class="brand__dot" aria-hidden="true"></span>Steadfast Money Partners</p>
      <p class="tagline">Choose your path, change your future.</p>
    </div>
  </article>
</section>

</body>
</html>
```